GUARANTEE PAY GIFT CARD DESIGN

This is a GIFT BONUS CARD

SIZE: 3.5INCH x 2INCH, 8.9cm x 5.1cm, DOUBLE SIDE
Orange must be used as an accent or primary colour.
#F37021, CMYK 0, 54, 86, 5

"BONUS CARD" AND "$20" MUST BE PART OF THE DESIGN.

Please see the attached logo
DO NOT use ribbons or gift box illustrations in the design.

***Terms and conditions must be on the back side of the card-
"No Cash Value. Card valid from 1/2/2024 to 3/31/2024. Valid for Riverside location only. Valid for Dine-in only. Not valid for online togo, delivery, or special events. "

Target Market(s)

40-60 YEARS OLD

Industry/Entity Type

Modern casual malaysian restaurant

Requirements
Must have
• ORANGE COLOUR, BONUS CARD, $20
Should not have
• Ribbons, gift box, CHOPSTICKS, BOWL, NOODLES, CHARATER ILLUSTRATIONS.

```html
<!DOCTYPE html>
<html lang="en">
<head>
<meta charset="utf-8">
<title>Lumo Kitchen Bonus Card</title>
<link rel="stylesheet" href="https://fonts.googleapis.com/css2?family=Barlow:wght@500&family=Barlow+Condensed:wght@400;500&family=Josefin+Sans:wght@400&display=swap">
<style>
  :root {
    --backdrop: #5a3d3f;
    --orange: #f7941e;
    --white: #ffffff;
    --green-dark: #37522f;
    --green: #3c9a46;
    --terms-ink: #3a4a30;
    --marker: #e8194f;
  }
  html, body {
    margin: 0;
    padding: 0;
    width: 1081px;
    height: 1200px;
    overflow: hidden;
    background: var(--backdrop);
  }
  .card {
    position: absolute;
    left: 169px;
    width: 742.5px;
    height: 432px;
    display: block;
  }
  .card--front { top: 166px; }
  .card--back { top: 612px; }
  .title { font-family: "Barlow", sans-serif; font-weight: 500; fill: var(--green-dark); }
  .amount { font-family: "Barlow Condensed", sans-serif; font-weight: 500; fill: var(--green); }
  .brand-name { font-family: "Josefin Sans", sans-serif; font-weight: 400; }
  .brand-name--light { fill: var(--white); }
  .brand-name--orange { fill: var(--orange); }
  .terms { font-family: "Barlow Condensed", sans-serif; font-weight: 400; fill: var(--terms-ink); }
</style>
</head>
<body>

<svg class="card card--front" viewBox="0 0 1075 626" aria-label="Bonus card front">
  <rect width="1075" height="626" fill="var(--orange)"/>
  <circle class="sweep-line" cx="700" cy="-40" r="640" fill="none" stroke="var(--white)" stroke-width="3"/>
  <circle class="value-disc" cx="908" cy="95" r="353" fill="var(--white)"/>
  <circle class="value-ring" cx="908" cy="95" r="297" fill="none" stroke="var(--orange)" stroke-width="4"/>
  <circle class="brand-ring" cx="300" cy="311" r="258" fill="var(--orange)" stroke="var(--white)" stroke-width="5"/>
  <text class="brand-name brand-name--light" x="100" y="282" font-size="100" textLength="280" lengthAdjust="spacing">LUMO</text>
  <text class="brand-name brand-name--light" x="100" y="378" font-size="92" textLength="410" lengthAdjust="spacingAndGlyphs">KITCHEN</text>
  <text class="title" x="1010" y="120" font-size="64" text-anchor="end">Bonus card</text>
  <text class="amount" x="935" y="305" font-size="205" text-anchor="end">20</text>
  <text class="amount" x="1010" y="262" font-size="105" text-anchor="end">$</text>
</svg>

<svg class="card card--back" viewBox="0 0 1075 626" aria-label="Bonus card back">
  <rect width="1075" height="626" fill="var(--white)"/>
  <circle class="sweep-line" cx="371" cy="-69" r="670" fill="none" stroke="var(--orange)" stroke-width="3"/>
  <circle class="plate-ring" cx="775" cy="311" r="258" fill="var(--white)" stroke="var(--orange)" stroke-width="6"/>
  <circle class="brand-ring" cx="775" cy="311" r="151" fill="none" stroke="var(--orange)" stroke-width="4"/>
  <text class="brand-name brand-name--orange" x="658" y="292" font-size="56" textLength="165" lengthAdjust="spacing">LUMO</text>
  <text class="brand-name brand-name--orange" x="658" y="351" font-size="52" textLength="240" lengthAdjust="spacingAndGlyphs">KITCHEN</text>

  <polygon class="marker" points="253,115 300,115 276,157" fill="var(--marker)"/>
  <polygon class="marker" points="253,475 300,475 276,434" fill="var(--marker)"/>
  <g class="terms" font-size="28" text-anchor="middle">
    <text x="276" y="202">No Cash Value!</text>
    <text x="276" y="242">Card valid from 1/2/2024 to 3/31/2024.</text>
    <text x="276" y="282">Valid for Riverside location only.</text>
    <text x="276" y="322">Valid for Dine-in only.</text>
    <text x="276" y="362">Not valid for online togo,</text>
    <text x="276" y="402">delivery, or special events.</text>
  </g>
</svg>

</body>
</html>
```